Life Coach for Lawyers Business Card Design

Elegant, original, business card design for life coaching service for associate attorneys who work in big law and struggle with stress, overwhelm, and time management. Double sided design.

Target Market(s)

Women associate attorneys who work in big law and struggle with stress, overwhelm, and time management.

Industry/Entity Type

Life Coaching

Contact Information for Business Card

Marissa Pendrell
Life Coach
518.677.3941
calmbriefcounsel.net
marissa@calmbriefcounsel.net
@calmbriefcounsel (Instagram)

Font styles to use
Other font styles liked:
• Silver South font duo. See uploaded files.

Requirements
Must have
• Icons for phone, website, email, and Instagram instead of words. Specific colors used in my logo (171B2B, 421121, FFFFFF)
Nice to have
• Foil. Embossed. Feminine design.
Should not have
• Any colors other than those used in logo. See uploaded files.

```html
<!DOCTYPE html>
<html lang="en">
<head>
<meta charset="utf-8">
<title>Calm Brief Counsel — Business Card</title>
<link href="https://fonts.googleapis.com/css2?family=Playfair+Display:wght@400;700&family=Libre+Baskerville:wght@400&display=swap" rel="stylesheet">
<style>
  :root{
    --navy:#171B2B;
    --maroon:#421121;
    --white:#FFFFFF;
    --paper:#ECEBE8;
    --backdrop:#D9D9DC;
  }
  html,body{margin:0;padding:0;overflow:hidden;}
  body{width:1200px;height:900px;background:var(--backdrop);position:relative;}
  .card{
    position:absolute;left:285px;width:630px;height:360px;
    box-shadow:0 6px 18px rgba(23,27,43,.18);
  }
  .card--front{top:60px;background:var(--navy);}
  .card--back{top:480px;background:var(--paper);}

  .front-mark{
    position:absolute;left:50%;top:50%;transform:translate(-50%,-50%);
    display:flex;align-items:center;gap:16px;white-space:nowrap;
  }
  .front-mark__circle{width:30px;height:30px;border-radius:50%;border:1.5px solid var(--white);flex:none;}
  .front-mark__name{
    font-family:"Playfair Display",serif;font-weight:400;font-size:28px;
    color:var(--white);letter-spacing:.08em;text-transform:uppercase;white-space:nowrap;
  }

  .back-brand{
    position:absolute;left:40px;top:190px;width:300px;
    font-family:"Playfair Display",serif;font-weight:400;font-size:30px;line-height:1.1;
    color:var(--maroon);letter-spacing:.04em;text-transform:uppercase;
  }
  .back-divider{position:absolute;left:360px;top:50px;width:1.5px;height:240px;background:var(--maroon);}

  .contact{position:absolute;left:384px;top:48px;}
  .contact__name{
    margin:0;font-family:"Playfair Display",serif;font-weight:700;font-size:24px;line-height:1.25;color:var(--navy);white-space:nowrap;
  }
  .contact__role{
    margin:0 0 18px;font-family:"Libre Baskerville",serif;font-size:15px;color:var(--maroon);
  }
  .contact__list{list-style:none;margin:0;padding:0;}
  .contact__item{
    display:flex;align-items:center;gap:12px;margin-bottom:16px;white-space:nowrap;
    font-family:"Libre Baskerville",serif;font-size:12px;color:var(--navy);
  }
  .contact__icon{width:22px;height:22px;flex:none;}
</style>
</head>
<body>
  <section class="card card--front" aria-label="Card front">
    <div class="front-mark">
      <span class="front-mark__circle"></span>
      <span class="front-mark__name">Calm Brief Counsel</span>
    </div>
  </section>

  <section class="card card--back" aria-label="Card back">
    <div class="back-brand">Calm Brief Counsel</div>
    <div class="back-divider"></div>
    <div class="contact">
      <h1 class="contact__name">Marissa Pendrell</h1>
      <p class="contact__role">Life Coach</p>
      <ul class="contact__list">
        <li class="contact__item">
          <svg class="contact__icon" viewBox="0 0 22 22" aria-hidden="true">
            <circle cx="11" cy="11" r="11" fill="#171B2B"/>
            <path d="M7.6 5.8c.5-.3 1-.2 1.3.2l1.1 1.7c.3.4.2 1-.2 1.3l-.7.5c.5 1.2 1.5 2.3 2.6 2.9l.5-.7c.3-.4.9-.5 1.3-.2l1.7 1.1c.4.3.5.8.2 1.3l-.6.9c-.4.6-1.2.9-1.9.6-2.8-1-4.9-3.2-5.9-6-.2-.7 0-1.4.6-1.8z" fill="#FFFFFF"/>
          </svg>
          518.677.3941
        </li>
        <li class="contact__item">
          <svg class="contact__icon" viewBox="0 0 22 22" aria-hidden="true">
            <circle cx="11" cy="11" r="11" fill="#171B2B"/>
            <rect x="5.5" y="7.5" width="11" height="7" fill="none" stroke="#FFFFFF" stroke-width="1.2"/>
            <polyline points="5.5,7.5 11,11.8 16.5,7.5" fill="none" stroke="#FFFFFF" stroke-width="1.2"/>
          </svg>
          marissa@calmbriefcounsel.net
        </li>
        <li class="contact__item">
          <svg class="contact__icon" viewBox="0 0 22 22" aria-hidden="true">
            <circle cx="11" cy="11" r="11" fill="#171B2B"/>
            <circle cx="11" cy="11" r="6" fill="none" stroke="#FFFFFF" stroke-width="1.1"/>
            <ellipse cx="11" cy="11" rx="2.6" ry="6" fill="none" stroke="#FFFFFF" stroke-width="1.1"/>
            <line x1="5" y1="11" x2="17" y2="11" stroke="#FFFFFF" stroke-width="1.1"/>
          </svg>
          calmbriefcounsel.net
        </li>
        <li class="contact__item">
          <svg class="contact__icon" viewBox="0 0 22 22" aria-hidden="true">
            <circle cx="11" cy="11" r="11" fill="#171B2B"/>
            <path d="M6 7.2h10v6.3H10l-2.6 2.2v-2.2H6z" fill="none" stroke="#FFFFFF" stroke-width="1.1" stroke-linejoin="round"/>
          </svg>
          @calmbriefcounsel
        </li>
      </ul>
    </div>
  </section>
</body>
</html>
```